Packaging & Label Design for CDB Products

We are a European CBD company specialising in athletic recovery, sleep improvement and wellness.

We would like the packaging to incorporate our logo and name (and font 'Codec') 'Meridell CBD'. The design must be transferable to all of our products. CBD Oils, Balms, Lip Balm and Vape E-Liquid.

We would like it to be simple but eye-catching and modern. We don't want bright colours. Preferred pallet of muted greys, blacks, white and pastel colours. Geometric concepts, possibly using different colours for each item of the range, we are open to new and fresh ideas (we are seeking you for your experience) and when we find the right design we would likely throw more work in your direction..

Our product range is not complete so the designer must be flexible with some changes and provide files where format can be easily edited by packaging manufacturer. We are also waiting for dimensions for the labels and boxes for several products and will supply the designer with full dimensions of all products once selected.

Oil Box: 2.6 x 9.0 x 2.6 cm (open format 16.7 x 11.6cm)
Labels: 7.8 x 3.3 cm (Front and Back)

Our expected product range will be:
CBD Oil 1000mg
CBD Oil 3000mg
CBD Balm 100mg
CBD Balm 300mg
E-Liquid 500mg
Lip Balm 50mg

We look forward to seeing your ideas.

Best Regards
Meridell CBD

```html
<!DOCTYPE html>
<html lang="en">
<head>
<meta charset="utf-8">
<title>Meridell CBD – Oil Label &amp; Box</title>
<link href="https://fonts.googleapis.com/css2?family=Montserrat:wght@300;400;600;700&display=swap" rel="stylesheet">
<style>
  :root {
    --page: #ffffff;
    --panel: #1e2321;
    --panel-deep: #191d1b;
    --ink: #ffffff;
    --muted: #9aa5a1;
    --accent: #3fa796;
    --cutline: #9a9a9a;
  }
  html, body {
    margin: 0;
    padding: 0;
    width: 1200px;
    height: 848px;
    overflow: hidden;
    background: var(--page);
  }
  .artboard {
    display: block;
    width: 1200px;
    height: 848px;
    font-family: "Montserrat", sans-serif;
  }
  .panel { fill: url(#panelTone); }
  .rule { stroke: var(--ink); stroke-width: 1; }
  .dieline { fill: none; stroke: var(--cutline); stroke-width: 1; stroke-dasharray: 4 3; }
  .badge { fill: none; stroke: var(--ink); stroke-width: 1.4; stroke-dasharray: 4 2; }
  .badge-small { fill: none; stroke: var(--ink); stroke-width: 1; stroke-dasharray: 2.5 1.5; }
  .variant { fill: var(--ink); font-weight: 300; }
  .brand-name { fill: var(--ink); font-weight: 700; letter-spacing: 1.5px; }
  .brand-sub { fill: var(--ink); font-weight: 700; letter-spacing: 5px; }
  .dose { fill: var(--ink); font-weight: 700; }
  .product-title { fill: var(--ink); font-weight: 700; }
  .product-title .tint { fill: var(--accent); }
  .body-copy { fill: var(--accent); font-weight: 400; opacity: 0.85; }
</style>
</head>
<body>
<svg class="artboard" viewBox="0 0 1440 1018" xmlns="http://www.w3.org/2000/svg">
  <defs>
    <linearGradient id="panelTone" x1="0" y1="0" x2="0" y2="1">
      <stop offset="0" stop-color="#222826"/>
      <stop offset="1" stop-color="#1a1e1c"/>
    </linearGradient>
  </defs>

  <!-- Back label -->
  <g class="label label-back">
    <rect class="panel" x="122" y="352" width="162" height="383" role="img" aria-label="Dark geometric hexagon pattern background"/>
    <line class="rule" x1="180" y1="352" x2="180" y2="685"/>
    <circle class="badge-small" cx="220" cy="370" r="7"/>
    <circle class="badge-small" cx="244" cy="370" r="7"/>
    <circle class="badge-small" cx="220" cy="395" r="7"/>
    <circle class="badge-small" cx="244" cy="395" r="7"/>
    <circle class="badge-small" cx="220" cy="420" r="7"/>
    <text class="product-title" font-size="10" transform="translate(166 688) rotate(-90)">Meridell CBD/ <tspan class="tint">CBD Oil 1000mg</tspan></text>
    <g class="body-copy" font-size="7.5">
      <text transform="translate(186 688) rotate(-90)">Full spectrum hemp extract in organic MCT oil, cold pressed</text>
      <text transform="translate(198 688) rotate(-90)">for a clean taste and steady daily wellness support.</text>
      <text transform="translate(210 688) rotate(-90)">Place drops under the tongue and hold for sixty seconds.</text>
      <text transform="translate(240 688) rotate(-90)">Store cool and dry, away from children and sunlight.</text>
    </g>
  </g>

  <!-- Front label -->
  <g class="label label-front">
    <rect class="panel" x="338" y="352" width="162" height="383" role="img" aria-label="Dark geometric hexagon pattern background"/>
    <line class="rule" x1="418" y1="352" x2="418" y2="394"/>
    <text class="variant" x="418" y="415" font-size="14" text-anchor="middle">Oil</text>
    <text class="brand-name" x="418" y="520" font-size="18" text-anchor="middle">MERIDELL</text>
    <text class="brand-sub" x="421" y="535" font-size="8" text-anchor="middle">CBD</text>
    <line class="rule" x1="418" y1="545" x2="418" y2="700"/>
    <text class="dose" x="418" y="722" font-size="11" text-anchor="middle">1000 mg</text>
  </g>

  <!-- Box dieline -->
  <g class="box">
    <path class="dieline" d="M709 290 L716 255 L716 228 L829 228 L829 255 L833 290"/>
    <path class="dieline" d="M972 290 L972 228 L1085 228 L1085 255 L1089 290"/>
    <path class="dieline" d="M1096 168 L1096 118 Q1096 100 1114 100 L1202 100 Q1220 100 1220 118 L1220 168 Z"/>
    <path class="dieline" d="M1217 290 L1240 290 L1280 300 L1280 720 L1240 730 L1217 730"/>
    <path class="dieline" d="M709 733 L716 765 L716 795 L829 795 L829 765 L833 733"/>
    <path class="dieline" d="M838 733 L838 855 L965 855 L965 733"/>
    <path class="dieline" d="M838 855 L838 902 Q838 920 856 920 L947 920 Q965 920 965 902 L965 855"/>
    <path class="dieline" d="M972 733 L972 795 L1085 795 L1085 765 L1089 733"/>
    <rect class="dieline" x="707" y="290" width="512" height="443"/>

    <!-- Top panel -->
    <rect class="panel" x="1096" y="172" width="120" height="113"/>
    <text class="brand-name" x="1156" y="233" font-size="15" text-anchor="middle">MERIDELL</text>

    <!-- Panel 1: side spine -->
    <rect class="panel" x="709" y="295" width="124" height="433" role="img" aria-label="Dark geometric hexagon pattern background"/>
    <line class="rule" x1="745" y1="295" x2="745" y2="330"/>
    <line class="rule" x1="797" y1="295" x2="797" y2="330"/>
    <text class="brand-name" font-size="15" transform="translate(750 690) rotate(-90)">MERIDELL</text>
    <text class="brand-sub" font-size="7" transform="translate(766 672) rotate(-90)">CBD</text>

    <!-- Panel 2: front -->
    <rect class="panel" x="838" y="295" width="124" height="433" role="img" aria-label="Dark geometric hexagon pattern background"/>
    <line class="rule" x1="902" y1="295" x2="902" y2="355"/>
    <text class="variant" x="901" y="377" font-size="13" text-anchor="middle">Oil</text>
    <text class="brand-name" x="901" y="495" font-size="14" text-anchor="middle">MERIDELL</text>
    <text class="brand-sub" x="903" y="507" font-size="6.5" text-anchor="middle">CBD</text>
    <line class="rule" x1="902" y1="516" x2="902" y2="700"/>
    <text class="dose" x="901" y="719" font-size="8" text-anchor="middle">1000 mg</text>

    <!-- Panel 3: badges -->
    <rect class="panel" x="967" y="295" width="122" height="433" role="img" aria-label="Dark geometric hexagon pattern background"/>
    <line class="rule" x1="985" y1="295" x2="985" y2="320"/>
    <line class="rule" x1="1047" y1="295" x2="1047" y2="320"/>
    <circle class="badge" cx="1005" cy="408" r="16"/>
    <circle class="badge" cx="1005" cy="453" r="16"/>
    <circle class="badge" cx="1005" cy="497" r="16"/>
    <circle class="badge" cx="1005" cy="543" r="16"/>
    <circle class="badge" cx="1005" cy="588" r="16"/>
    <line class="rule" x1="1005" y1="612" x2="1005" y2="728"/>
    <line class="rule" x1="1047" y1="705" x2="1047" y2="728"/>

    <!-- Panel 4: back info -->
    <rect class="panel" x="1096" y="295" width="121" height="433" role="img" aria-label="Dark geometric hexagon pattern background"/>
    <line class="rule" x1="1130" y1="295" x2="1130" y2="728"/>
    <text class="product-title" font-size="10" transform="translate(1118 716) rotate(-90)">Meridell CBD/ <tspan class="tint">CBD Oil 1000mg</tspan></text>
    <g class="body-copy" font-size="7.5">
      <text transform="translate(1140 716) rotate(-90)">Full spectrum hemp extract in organic MCT oil, cold pressed</text>
      <text transform="translate(1152 716) rotate(-90)">for a clean taste and steady daily wellness support.</text>
      <text transform="translate(1164 716) rotate(-90)">Place drops under the tongue and hold for sixty seconds.</text>
      <text transform="translate(1190 716) rotate(-90)">Store cool and dry, away from children and sunlight.</text>
    </g>
  </g>
</svg>
</body>
</html>
```